Stationery Set for BRV Company

I need to create full stationery design for my company; Business Cards, Envelops, Letter Heads, Calendar.
In the letter head and Envelops... only contact information and website links.
Our company is a Service Management company with different domains of innovative services including Technology Service Management, Education Services, Outsourcing Management, Events Management.
I need a modern and innovative design specially for the business card. I some transparent designs and I like it, but don't limit your innovation to what I mentioned. Sky is limit for your innovation.

Target Market(s)

Middle East & Africa

Industry/Entity Type

Business Management

Colors
34a7d8
0355a3
85acd3
86cae7
cee9f5
cfdeed
e4daeb
f3f1f8
ecf7fb

Requirements
Must have
• Name, Title, Email, Mobile
Nice to have
• We have multiple locations in USA, KSA, EGY, so I need ideas about how to include all contact details maybe QR / Barcode or something else.
• Please see our locations and contact information: www.ploventa.com
Should not have
• Too much text

```html
<!DOCTYPE html>
<html lang="en">
<head>
<meta charset="utf-8">
<title>BRV Company – Window Envelope</title>
<link href="https://fonts.googleapis.com/css2?family=Quicksand:wght@500;700&display=swap" rel="stylesheet">
<style>
  :root {
    --page: #ffffff;
    --silver-dark: #c9c6c3;
    --silver-mid: #dcdad8;
    --silver-light: #f1f0ef;
    --band: #ececec;
    --band-edge: #8f8f8f;
    --window: #ffffff;
    --window-edge: #3a3a3a;
    --brand-grey: #8c8c8c;
    --address-blue: #2b9fd9;
    --swoosh: #d3d1cf;
  }
  html, body {
    margin: 0;
    padding: 0;
    width: 1200px;
    height: 1000px;
    overflow: hidden;
    background: var(--page);
  }
  .canvas {
    position: relative;
    width: 1200px;
    height: 1000px;
  }
  .envelope {
    position: absolute;
    left: 35px;
    top: 220px;
    width: 1143px;
    height: 570px;
    overflow: hidden;
    background:
      linear-gradient(100deg,
        var(--silver-dark) 0%,
        var(--silver-mid) 12%,
        var(--silver-light) 22%,
        var(--silver-mid) 32%,
        var(--silver-dark) 42%,
        var(--silver-mid) 55%,
        var(--silver-light) 68%,
        var(--silver-mid) 78%,
        var(--silver-dark) 90%,
        var(--silver-mid) 100%);
    box-shadow: 1px 2px 3px rgba(0,0,0,0.45);
  }
  .envelope__swoosh {
    position: absolute;
    left: 0;
    top: 30px;
    width: 480px;
    height: 230px;
  }
  .envelope__band {
    position: absolute;
    left: 0;
    top: 440px;
    width: 100%;
    height: 46px;
    background: linear-gradient(90deg, var(--band) 0%, #f7f7f7 40%, var(--band) 60%, #f5f5f5 100%);
    border-top: 1px solid var(--band-edge);
    border-bottom: 1px solid var(--band-edge);
  }
  .envelope__window {
    position: absolute;
    left: 622px;
    top: 308px;
    width: 468px;
    height: 196px;
    background: var(--window);
    border: 1px solid var(--window-edge);
    border-radius: 14px;
  }
  .brand-name {
    position: absolute;
    left: 72px;
    top: 78px;
    margin: 0;
    font-family: "Quicksand", sans-serif;
    font-weight: 700;
    font-size: 46px;
    line-height: 1;
    letter-spacing: -0.5px;
    color: var(--brand-grey);
  }
  .sender-address {
    position: absolute;
    left: 74px;
    top: 202px;
    margin: 0;
    font-family: "Quicksand", sans-serif;
    font-weight: 500;
    font-style: normal;
    font-size: 18px;
    line-height: 29px;
    color: var(--address-blue);
  }
</style>
</head>
<body>
  <div class="canvas">
    <div class="envelope">
      <svg class="envelope__swoosh" viewBox="0 0 480 230" role="img" aria-label="Faint decorative wave lines in light silver">
        <defs>
          <linearGradient id="swooshTone" x1="0" y1="0" x2="1" y2="0">
            <stop offset="0" stop-color="var(--swoosh)" stop-opacity="0.7"/>
            <stop offset="1" stop-color="var(--swoosh)" stop-opacity="0"/>
          </linearGradient>
        </defs>
        <path d="M0 0 C120 20 260 40 480 0 C380 90 200 140 0 230 Z" fill="url(#swooshTone)"/>
      </svg>

      <p class="brand-name">BRV Company</p>

      <address class="sender-address">
        418 Harbor Point Road, 6th<br>
        Floor Lakemont City CA 94170<br>
        US
      </address>

      <div class="envelope__band"></div>
      <div class="envelope__window"></div>
    </div>
  </div>
</body>
</html>
```